Velvet Crown Tresses price sheet/brochure

So I'm looking to create a pricing sheet/brochure for my hair company. The company name is "Velvet Crown Tresses" and we specialize in providing Peruvian, Brazilian and Indian weave hair. I created a logo some time ago that I'd like to use if possible. If not, I'll need to create a logo as well!

8.5 x 11....not sure how many pages are needed to properly display all pricing, but I'd like the pricing to be at a size that makes it easy for the client to read. Open A-3

Target Market(s)

Hair stylist as well as their clients. Looking to establish business in Africa as well!

Industry/Entity Type

Hair And Beauty

Font styles to use
Serif

Colors
e34298

Requirements
Must have
• Price sheet/brochure must be easy to read and give potential client all the pertinent information needed regarding our hair! Also want the brochure to present style and pride in the excellent quality hair the "Velvet Crown Tresses"! 😀
• Velvet Crown Tresses
• Base price for all hair textures. Pricing will increase depending on wave pattern.
• Peruvian & Brazilian Virgin Hair
• 4 bundle deals
• 10, 12, 14, 16 - $405
• 12, 14, 16, 18 - $434
• 14, 16, 18, 20 - $467
• 16, 18, 20, 22 - $504
• 18, 20, 22, 24 - $539
• 20, 22, 24, 26 - $576
• 22, 24, 26, 28 - $621
• 24, 26, 28, 30 - $660
• 26, 28, 30, 32 - $693
• 28, 30, 32, 34 - $728
• 30, 32, 34, 36 - $760
• 32, 34, 36, 38 - $799
• 3 bundle deals
• 10, 12, 14 - $281
• 12, 14, 16 - $333
• 14, 16, 18 - $358
• 16, 18, 20 - $385
• 18, 20, 22 - $410
• 20, 22, 24 - $432
• 22, 24, 26 - $471
• 24, 26, 28 - $500
• 26, 28, 30 - $533
• 28, 30, 32 - $560
• 30, 32, 34 - $589
• 32, 34, 36 - $608
• 34, 36, 38 - $635
• 2 Bundles
• 2 Bundles 10 - $203
• 2 Bundles 12 - $235
• 2 Bundles 14 - $251
• 2 Bundles 16 - $272
• 2 Bundles 18 - $285
• 2 Bundles 20 - $302
• 2 Bundles 22 - $346
• 2 Bundles 24 - $345
• 2 Bundles 26 - $357
• 2 Bundles 28 - $384
• 2 Bundles 30 - $418
• 2 Bundles 32 - $429
• 2 Bundles 34 - $440
• 2 Bundles 36 - $476
• 2 Bundles 38 - $502
• 1 Bundle
• 1 Bundle 10 - $97
• 1 Bundle 12 - $110
• 1 Bundle 14 - $116
• 1 Bundle 16 - $126
• 1 Bundle 18 - $134
• 1 Bundle 20 - $141
• 1 Bundle 22 - $154
• 1 Bundle 24 - $167
• 1 Bundle 26 - $172
• 1 Bundle 28 - $185
• 1 Bundle 30 - $192
• 1 Bundle 32 - $197
• 1 Bundle 34 - $205
• 1 Bundle 36 - $215
• 1 Bundle 38 - $230
• -----------------------------------------------------------------------------
• Indian Virgin Hair
• 4 bundle deals
• 10, 12, 14, 16 - $293
• 12, 14, 16, 18 - $314
• 14, 16, 18, 20 - $325
• 16, 18, 20, 22 - $348
• 18, 20, 22, 24 - $367
• 20, 22, 24, 26 - $386
• 22, 24, 26, 28 - $407
• 24, 26, 28, 30 - $425
• 26, 28, 30, 32 - $444
• 28, 30, 32, 34 - $461
• 30, 32, 34, 36 - $477
• 32, 34, 36, 38 - $495
• 3 bundle deals
• 10, 12, 14 - $223
• 12, 14, 16 - $239
• 14, 16, 18 - $252
• 16, 18, 20 - $264
• 18, 20, 22 - $278
• 20, 22, 24 - $293
• 22, 24, 26 - $308
• 24, 26, 28 - $322
• 26, 28, 30 - $337
• 28, 30, 32 - $350
• 30, 32, 34 - $262
• 32, 34, 36 - $375
• 34, 36, 38 - $390
• 2 Bundles
• 2 Bundles 10 - $74
• 2 Bundles 12 - $90
• 2 Bundles 14 - $98
• 2 Bundles 16 - $107
• 2 Bundles 18 - $115
• 2 Bundles 20 - $123
• 2 Bundles 22 - $135
• 2 Bundles 24 - $143
• 2 Bundles 26 - $154
• 2 Bundles 28 - $164
• 2 Bundles 30 - $172
• 2 Bundles 32 - $180
• 2 Bundles 34 - $189
• 2 Bundles 36 - $197
• 2 Bundles 38 - $207
• 1 Bundle
• 1 Bundle 10 - $80
• 1 Bundle 12 - $88
• 1 Bundle 14 - $93
• 1 Bundle 16 - $98
• 1 Bundle 18 - $102
• 1 Bundle 20 - $109
• 1 Bundle 22 - $115
• 1 Bundle 24 - $122
• 1 Bundle 26 - $130
• 1 Bundle 28 - $137
• 1 Bundle 30 - $144
• 1 Bundle 32 - $156
• 1 Bundle 34 - $163
• 1 Bundle 36 - $175
• 1 Bundle 38 - $190
• Hair Care
• It's very important to take good care of your hair to keep using long time, below are some brief introduction
• IMPORTANT: Treat 100% human hair extensions gently.
• 1. Wash and condition hair regularly, at maximum of 3 times a week. This will keep the moisture in from shampooing while at the same time not drying them out from over shampooing.
• 2. Combing hair gently before washing. Do not rub or twist hair.
• 3. Add mild shampoo to cool water or warm water about 35℃ (Please do not use hot water) and swish hair till clean. Rinse thoroughly.
• 4. Blot out excess water with towel and allow hair to dry naturally. Do not expose to sun
• 5. Comb curly hair gently with your fingers from end to top. Do not brush
• 6. Hair may be tangled if general care directions are not followed properly.
• Important Note:
• Brush the end of hair first, then the middle, and the top at last. DO NOT brush directly from the top and pull hard, it will break the hair. Regular care will keep the hair in good condition and avoid tangle problem, improper dyeing or other chemical process will damage the hair and cause tangle and shedding problem. Please wash the hair with warm water before proceeding dyeing.
• Details of Hair Extension Maintenance Tips
• Straight Hair:
• Maintenance
• • Shampoo at least once a week.
• • Use a shampoo no higher than pH 7.
• • Dilute one ounce of shampoo in a bowl or jug with a pint of warm water.
• • Sponge the shampoo into the hair.
• • Do not massage.
• • Rinse thoroughly.
• • Apply conditioner and comb hair, starting with the ends working your way up to your scalp.
• • Rinse thoroughly.
• • Let air-dry.
• Daily
• • Brush or comb through to style.
• • Use styling aids, such as mouse, gel, and hairspray in moderation (preferably alcohol free products).
• Sleep
• • Before going to bed, braid your hair into one loose large braid at the back of the neck.
• • After waking up, undo braid and comb through beginning at the ends and working your way up to roots.
• Natural Body Wave Hair
• Maintenance
• • Do not massage.
• • Rinse thoroughly.
• • Rinse thoroughly.
• • Let air-dry.
• • Style as desired.
• • For extra wave, hair can be set in rollers.
• Daily
• Sleep
• • After waking up, undo braid.
• • Dampen hair with a water bottle.
• • Comb through beginning at the ends and working your way up to roots.
• • Let hair air-dry.
• • Style as desired.
• For extra wave, hair can be set in rollers.
• Permed Curly and Natural Curly Hair
• Maintenance
• • Do not use oil products on permed hair, it can cause matting.
• • Do not brush or comb hair when dry, it will cause frizz and the ends may tangle.
• • Do not massage.
• • Rinse thoroughly.
• • Rinse thoroughly.
• • Scrunch up hair gently to reform curl.
• • Let air-dry.
• • Style as desired.
• Daily
• Sleep
• • Let hair air-dry.
• • Style as desired.
• Specific Conditions
• Static:
• • In colder months, you may experience some static. The best way to deal with this is to dampen your hands with water, and rub hand together so they are warm. Run the palms of your hands over your hair, without actually touching your hair. This process should help control the static.
• Swimming:
• It is not recommended that you swim with extension hair. However if you do the following precautions are recommended.
• • Never wear a swimming cap or anything that covers your hair, the friction may cause matting.
• • Before swimming comb out tangles.
• • Braid hair into one braid at back of neck.
• • Try to keep head above water.
• • Do not swim under water.
• • No diving.
• • After swimming keep head out of shower.
• • Immediately after showering undo braid, comb hair and let air-dry.
• • Follow with appropriate shampooing and conditioning as needed.
• Sauna:
• • The water of the sauna will penetrate the hair and wet it.
• • Do not wrap hair in towel, which will compress it.
• • After sauna keep head out of shower.
• Sunbathing:
• • After sunbathing do not unbraid until hair has cooled down.
• • After hair cools, undo braid, comb hair.
• Miscellaneous Tips:
• • Although the extension hair is real, it is not receiving nutrients from the scalp like your own hair. Heat is your hair extensions biggest enemy. The more you use on it, the shorter the life span of your hair. We cannot guarantee that the hair will remain silky if you use the blow dry, flat iron, or curling iron often.
• • When you sleep, we highly recommend that you braid, wrap or ponytail your hair together to prevent tangling. This will save time that would be spent untangling the hair the next morning.
• • When washing the hair, always wash it going in a downward motion. Use your fingers in a horizontal motion between wefts to clean your scalp. When rinsing, do the same to be sure that all the shampoo and conditioner residues are washed out.
• Sent from my Tablo
Nice to have
• Ditto....tried to upload logo but it was to big. Please advise!
Should not have
• Ditto....

```html
<!DOCTYPE html>
<html lang="en">
<head>
<meta charset="utf-8">
<title>Velvet Crown Tresses – Price Brochure</title>
<link href="https://fonts.googleapis.com/css2?family=Open+Sans:wght@400;600;700;800&family=Lora:ital,wght@0,400;0,700;1,400&display=swap" rel="stylesheet">
<style>
:root{
  --pink:#e34298;
  --pink-deep:#c42a7d;
  --pink-soft:#f6c3dd;
  --pink-mist:#fbe6f1;
  --ink:#3a3a3a;
  --muted:#6b6b6b;
  --paper:#ffffff;
  --rule:#e9b3cf;
}
*{box-sizing:border-box;margin:0;padding:0}
html,body{width:802px;height:1200px;overflow:hidden;background:var(--paper)}
body{position:relative;font-family:"Open Sans",Arial,sans-serif;color:var(--ink)}
.spread{position:absolute;left:27px;width:748px;height:270px;display:flex;gap:4px}
.spread--cover{top:18px}
.spread--prices{top:314px}
.spread--care{top:610px}
.spread--tips{top:906px}
.page{position:relative;width:372px;height:270px;background:var(--paper);overflow:hidden;box-shadow:0 0 0 1px #eee}
.page--pinkfoot{background:linear-gradient(180deg,#fff 0%,#fff 45%,var(--pink-mist) 70%,var(--pink-soft) 100%)}
.photo{position:absolute}
.brand{font-family:"Lora",Georgia,serif;font-weight:700;color:var(--pink);display:flex;align-items:center;gap:4px;white-space:nowrap}
.brand::before{content:"";width:6px;height:6px;border-radius:50%;background:var(--pink)}
.tagline{font-family:"Lora",Georgia,serif;font-style:italic;color:var(--muted)}

/* cover */
.cover-photo{inset:0;background:linear-gradient(120deg,#f4f0ee 0%,#e8ded9 35%,#5a3a2c 55%,#2a1a14 75%,#f4f0ee 100%)}
.cover-brand{position:absolute;right:16px;bottom:48px;font-size:14px}
.cover-tag{position:absolute;right:16px;bottom:30px;font-size:8px}
.back-swirl{position:absolute;left:0;right:0;bottom:0;height:120px;background:radial-gradient(ellipse at 80% 110%,var(--pink-soft) 0%,var(--pink-mist) 45%,rgba(255,255,255,0) 75%)}
.back-block{position:absolute;left:0;right:0;top:70px;text-align:center}
.back-block .brand{justify-content:center;font-size:16px}
.back-block .tagline{display:block;font-size:7.5px;margin-top:5px}
.back-block .email{display:block;font-size:6.5px;color:var(--muted);margin-top:3px}

/* prices */
.title-bar{position:absolute;top:12px;left:0;right:0;height:22px;background:linear-gradient(90deg,var(--pink-mist),var(--pink-soft),var(--pink-mist));display:flex;align-items:center;justify-content:center;font-family:"Lora",Georgia,serif;font-weight:700;font-size:12px;color:var(--ink)}
.price-grid{position:absolute;top:42px;display:flex;gap:4px}
.price-grid--left{right:10px}
.price-grid--right{left:10px}
.price-table{border-collapse:collapse;font-size:5.2px;width:66px}
.price-table caption{font-size:6px;font-weight:700;color:var(--pink);padding-bottom:2px;text-align:left}
.price-table th{background:var(--pink);color:#fff;font-weight:700;padding:1.5px 2px;text-align:left}
.price-table td{padding:1.6px 2px;border-bottom:1px solid var(--rule);white-space:nowrap}
.price-table tr:nth-child(even) td{background:var(--pink-mist)}
.price-table td:last-child{text-align:right;font-weight:700}
.hair-left{left:6px;top:60px;width:62px;height:190px;background:linear-gradient(180deg,#2b2624,#0f0d0c 60%,#3b332f)}
.hair-right{right:6px;top:60px;width:62px;height:190px;background:linear-gradient(180deg,#3a2f2a,#120f0e 55%,#3b322e)}

/* hair care */
.heading{font-weight:800;color:var(--ink);font-size:12px}
.care-head{position:absolute;left:12px;top:14px}
.care-intro{position:absolute;left:12px;top:32px;width:150px;font-size:5.2px;line-height:1.35;color:var(--muted)}
.care-list{position:absolute;left:12px;top:60px;width:150px;font-size:5.2px;line-height:1.4;list-style:none}
.care-list li{margin-bottom:3px;padding-left:6px;position:relative}
.care-list li::before{content:"";position:absolute;left:0;top:2px;width:3px;height:3px;background:var(--pink);border-radius:50%}
.care-photo{left:180px;top:14px;width:178px;height:90px;background:linear-gradient(180deg,#2a2422,#0d0b0a 60%,#2e2724)}
.note-box{position:absolute;left:180px;top:112px;width:178px;padding:6px;background:var(--pink);color:#fff;font-size:5.2px;line-height:1.4}
.note-box strong{display:block;font-size:6.5px;margin-bottom:2px}
.care-brand{position:absolute;right:14px;bottom:14px;font-size:10px}
.maint-head{position:absolute;left:12px;top:14px;font-size:11px}
.maint-brand{position:absolute;right:12px;top:14px;font-size:8px}
.maint-cols{position:absolute;left:12px;right:12px;top:34px;display:flex;gap:8px}
.maint-col{flex:1;font-size:4.6px;line-height:1.3}
.maint-col h4{font-size:6px;color:var(--pink);margin-bottom:2px}
.maint-col h5{font-size:5px;font-weight:700;margin:2px 0 1px}
.maint-col ul{list-style:none}

/* specific conditions */
.spec-head{position:absolute;left:12px;top:14px}
.spec-photo{left:170px;top:12px;width:80px;height:70px;background:linear-gradient(180deg,#2e2725,#0e0c0b 60%,#332b28)}
.spec-cols{position:absolute;left:12px;right:12px;top:90px;display:flex;gap:12px}
.spec-col{flex:1;font-size:4.8px;line-height:1.35}
.spec-col h4{font-size:6px;color:var(--pink);margin:3px 0 1px}
.spec-col ul{list-style:none}
.misc-photo{left:0;top:0;width:180px;height:270px;background:linear-gradient(160deg,#f2eeec 0%,#a0663f 40%,#6b3a1f 70%,#f2eeec 100%)}
.misc-head{position:absolute;left:192px;top:14px}
.misc-text{position:absolute;left:192px;top:34px;width:168px;font-size:5.2px;line-height:1.4;list-style:none}
.misc-text li{margin-bottom:5px}
.misc-brand{position:absolute;right:12px;bottom:14px;font-size:9px}
</style>
</head>
<body>

<!-- Cover spread -->
<section class="spread spread--cover">
  <div class="page page--front">
    <div class="photo cover-photo" role="img" aria-label="Portrait of a model with long curly black hair"></div>
    <div class="brand cover-brand">Velvet Crown Tresses</div>
    <div class="tagline cover-tag">Beauty • Excellence • Quality</div>
  </div>
  <div class="page page--back">
    <div class="back-swirl"></div>
    <div class="back-block">
      <div class="brand">Velvet Crown Tresses</div>
      <span class="tagline">Beauty • Excellence • Quality</span>
      <span class="email">hello@velvetcrowntresses.com</span>
    </div>
  </div>
</section>

<!-- Price spread -->
<section class="spread spread--prices">
  <div class="page page--pinkfoot">
    <div class="title-bar">Peruvian &amp; Brazilian Virgin Hair</div>
    <div class="photo hair-left" role="img" aria-label="Bundles of straight and wavy black hair"></div>
    <div class="price-grid price-grid--left">
      <table class="price-table"><caption>4 Bundle Deals</caption><tr><th>Length</th><th>Price</th></tr>
        <tr><td>10,12,14,16</td><td>$405</td></tr><tr><td>12,14,16,18</td><td>$434</td></tr><tr><td>14,16,18,20</td><td>$467</td></tr><tr><td>16,18,20,22</td><td>$504</td></tr><tr><td>18,20,22,24</td><td>$539</td></tr><tr><td>20,22,24,26</td><td>$576</td></tr><tr><td>22,24,26,28</td><td>$621</td></tr><tr><td>24,26,28,30</td><td>$660</td></tr><tr><td>26,28,30,32</td><td>$693</td></tr><tr><td>28,30,32,34</td><td>$728</td></tr><tr><td>30,32,34,36</td><td>$760</td></tr><tr><td>32,34,36,38</td><td>$799</td></tr></table>
      <table class="price-table"><caption>3 Bundle Deals</caption><tr><th>Length</th><th>Price</th></tr>
        <tr><td>10,12,14</td><td>$281</td></tr><tr><td>12,14,16</td><td>$333</td></tr><tr><td>14,16,18</td><td>$358</td></tr><tr><td>16,18,20</td><td>$385</td></tr><tr><td>18,20,22</td><td>$410</td></tr><tr><td>20,22,24</td><td>$432</td></tr><tr><td>22,24,26</td><td>$471</td></tr><tr><td>24,26,28</td><td>$500</td></tr><tr><td>26,28,30</td><td>$533</td></tr><tr><td>28,30,32</td><td>$560</td></tr><tr><td>30,32,34</td><td>$589</td></tr><tr><td>32,34,36</td><td>$608</td></tr><tr><td>34,36,38</td><td>$635</td></tr></table>
      <table class="price-table"><caption>2 Bundles</caption><tr><th>Length</th><th>Price</th></tr>
        <tr><td>10"</td><td>$203</td></tr><tr><td>12"</td><td>$235</td></tr><tr><td>14"</td><td>$251</td></tr><tr><td>16"</td><td>$272</td></tr><tr><td>18"</td><td>$285</td></tr><tr><td>20"</td><td>$302</td></tr><tr><td>22"</td><td>$346</td></tr><tr><td>24"</td><td>$345</td></tr><tr><td>26"</td><td>$357</td></tr><tr><td>28"</td><td>$384</td></tr><tr><td>30"</td><td>$418</td></tr><tr><td>32"</td><td>$429</td></tr><tr><td>34"</td><td>$440</td></tr><tr><td>36"</td><td>$476</td></tr><tr><td>38"</td><td>$502</td></tr></table>
      <table class="price-table"><caption>1 Bundle</caption><tr><th>Length</th><th>Price</th></tr>
        <tr><td>10"</td><td>$97</td></tr><tr><td>12"</td><td>$110</td></tr><tr><td>14"</td><td>$116</td></tr><tr><td>16"</td><td>$126</td></tr><tr><td>18"</td><td>$134</td></tr><tr><td>20"</td><td>$141</td></tr><tr><td>22"</td><td>$154</td></tr><tr><td>24"</td><td>$167</td></tr><tr><td>26"</td><td>$172</td></tr><tr><td>28"</td><td>$185</td></tr><tr><td>30"</td><td>$192</td></tr><tr><td>32"</td><td>$197</td></tr><tr><td>34"</td><td>$205</td></tr><tr><td>36"</td><td>$215</td></tr><tr><td>38"</td><td>$230</td></tr></table>
    </div>
  </div>
  <div class="page page--pinkfoot">
    <div class="title-bar">Indian Virgin Hair</div>
    <div class="photo hair-right" role="img" aria-label="Bundles of loose wave black hair"></div>
    <div class="price-grid price-grid--right">
      <table class="price-table"><caption>4 Bundle Deals</caption><tr><th>Length</th><th>Price</th></tr>
        <tr><td>10,12,14,16</td><td>$293</td></tr><tr><td>12,14,16,18</td><td>$314</td></tr><tr><td>14,16,18,20</td><td>$325</td></tr><tr><td>16,18,20,22</td><td>$348</td></tr><tr><td>18,20,22,24</td><td>$367</td></tr><tr><td>20,22,24,26</td><td>$386</td></tr><tr><td>22,24,26,28</td><td>$407</td></tr><tr><td>24,26,28,30</td><td>$425</td></tr><tr><td>26,28,30,32</td><td>$444</td></tr><tr><td>28,30,32,34</td><td>$461</td></tr><tr><td>30,32,34,36</td><td>$477</td></tr><tr><td>32,34,36,38</td><td>$495</td></tr></table>
      <table class="price-table"><caption>3 Bundle Deals</caption><tr><th>Length</th><th>Price</th></tr>
        <tr><td>10,12,14</td><td>$223</td></tr><tr><td>12,14,16</td><td>$239</td></tr><tr><td>14,16,18</td><td>$252</td></tr><tr><td>16,18,20</td><td>$264</td></tr><tr><td>18,20,22</td><td>$278</td></tr><tr><td>20,22,24</td><td>$293</td></tr><tr><td>22,24,26</td><td>$308</td></tr><tr><td>24,26,28</td><td>$322</td></tr><tr><td>26,28,30</td><td>$337</td></tr><tr><td>28,30,32</td><td>$350</td></tr><tr><td>30,32,34</td><td>$262</td></tr><tr><td>32,34,36</td><td>$375</td></tr><tr><td>34,36,38</td><td>$390</td></tr></table>
      <table class="price-table"><caption>2 Bundles</caption><tr><th>Length</th><th>Price</th></tr>
        <tr><td>10"</td><td>$74</td></tr><tr><td>12"</td><td>$90</td></tr><tr><td>14"</td><td>$98</td></tr><tr><td>16"</td><td>$107</td></tr><tr><td>18"</td><td>$115</td></tr><tr><td>20"</td><td>$123</td></tr><tr><td>22"</td><td>$135</td></tr><tr><td>24"</td><td>$143</td></tr><tr><td>26"</td><td>$154</td></tr><tr><td>28"</td><td>$164</td></tr><tr><td>30"</td><td>$172</td></tr><tr><td>32"</td><td>$180</td></tr><tr><td>34"</td><td>$189</td></tr><tr><td>36"</td><td>$197</td></tr><tr><td>38"</td><td>$207</td></tr></table>
      <table class="price-table"><caption>1 Bundle</caption><tr><th>Length</th><th>Price</th></tr>
        <tr><td>10"</td><td>$80</td></tr><tr><td>12"</td><td>$88</td></tr><tr><td>14"</td><td>$93</td></tr><tr><td>16"</td><td>$98</td></tr><tr><td>18"</td><td>$102</td></tr><tr><td>20"</td><td>$109</td></tr><tr><td>22"</td><td>$115</td></tr><tr><td>24"</td><td>$122</td></tr><tr><td>26"</td><td>$130</td></tr><tr><td>28"</td><td>$137</td></tr><tr><td>30"</td><td>$144</td></tr><tr><td>32"</td><td>$156</td></tr><tr><td>34"</td><td>$163</td></tr><tr><td>36"</td><td>$175</td></tr><tr><td>38"</td><td>$190</td></tr></table>
    </div>
  </div>
</section>

<!-- Care spread -->
<section class="spread spread--care">
  <div class="page page--pinkfoot">
    <h2 class="heading care-head">Hair Care</h2>
    <p class="care-intro">It's very important to take good care of your hair to keep using long time, below are some brief introduction. <strong>IMPORTANT:</strong> Treat 100% human hair extensions gently.</p>
    <ol class="care-list">
      <li>Wash and condition hair regularly, at maximum of 3 times a week. This will keep the moisture in from shampooing while not drying them out.</li>
      <li>Combing hair gently before washing. Do not rub or twist hair.</li>
      <li>Add mild shampoo to cool or warm water about 35℃ (please do not use hot water) and swish hair till clean. Rinse thoroughly.</li>
      <li>Blot out excess water with towel and allow hair to dry naturally. Do not expose to sun.</li>
      <li>Comb curly hair gently with your fingers from end to top. Do not brush.</li>
      <li>Hair may be tangled if general care directions are not followed properly.</li>
    </ol>
    <div class="photo care-photo" role="img" aria-label="Three bundles of straight black hair"></div>
    <div class="note-box"><strong>Important Note:</strong>Brush the end of hair first, then the middle, and the top at last. DO NOT brush directly from the top and pull hard, it will break the hair. Regular care will keep the hair in good condition and avoid tangle problems. Improper dyeing or other chemical process will damage the hair and cause tangle and shedding. Please wash the hair with warm water before dyeing.</div>
    <div class="brand care-brand">Velvet Crown Tresses</div>
  </div>
  <div class="page page--pinkfoot">
    <h2 class="heading maint-head">Details of Hair Extension Maintenance Tips</h2>
    <div class="brand maint-brand">Velvet Crown Tresses</div>
    <div class="maint-cols">
      <div class="maint-col">
        <h4>Straight Hair</h4>
        <h5>Maintenance</h5>
        <ul><li>• Shampoo at least once a week.</li><li>• Use a shampoo no higher than pH 7.</li><li>• Dilute one ounce of shampoo in a jug with a pint of warm water.</li><li>• Sponge the shampoo into the hair.</li><li>• Do not massage.</li><li>• Rinse thoroughly.</li><li>• Apply conditioner and comb hair, starting with the ends working up to your scalp.</li><li>• Rinse thoroughly.</li><li>• Let air-dry.</li></ul>
        <h5>Daily</h5>
        <ul><li>• Brush or comb through to style.</li><li>• Use styling aids such as mousse, gel and hairspray in moderation (preferably alcohol free).</li></ul>
        <h5>Sleep</h5>
        <ul><li>• Before bed, braid hair into one loose large braid at the back of the neck.</li><li>• After waking up, undo braid and comb through from the ends up to roots.</li></ul>
      </div>
      <div class="maint-col">
        <h4>Natural Body Wave Hair</h4>
        <h5>Maintenance</h5>
        <ul><li>• Do not massage.</li><li>• Rinse thoroughly.</li><li>• Rinse thoroughly.</li><li>• Let air-dry.</li><li>• Style as desired.</li><li>• For extra wave, hair can be set in rollers.</li></ul>
        <h5>Daily</h5>
        <h5>Sleep</h5>
        <ul><li>• After waking up, undo braid.</li><li>• Dampen hair with a water bottle.</li><li>• Comb through beginning at the ends and working up to roots.</li><li>• Let hair air-dry.</li><li>• Style as desired.</li><li>• For extra wave, hair can be set in rollers.</li></ul>
      </div>
      <div class="maint-col">
        <h4>Permed Curly &amp; Natural Curly Hair</h4>
        <h5>Maintenance</h5>
        <ul><li>• Do not use oil products on permed hair, it can cause matting.</li><li>• Do not brush or comb hair when dry, it will cause frizz and the ends may tangle.</li><li>• Do not massage.</li><li>• Rinse thoroughly.</li><li>• Rinse thoroughly.</li><li>• Scrunch up hair gently to reform curl.</li><li>• Let air-dry.</li><li>• Style as desired.</li></ul>
        <h5>Daily</h5>
        <h5>Sleep</h5>
        <ul><li>• Let hair air-dry.</li><li>• Style as desired.</li></ul>
      </div>
    </div>
  </div>
</section>

<!-- Tips spread -->
<section class="spread spread--tips">
  <div class="page page--pinkfoot">
    <h2 class="heading spec-head">Specific Conditions</h2>
    <div class="photo spec-photo" role="img" aria-label="Bundle of deep wave black hair"></div>
    <div class="spec-cols">
      <div class="spec-col">
        <h4>Static</h4>
        <ul><li>• In colder months you may experience some static. Dampen your hands with water and rub them together so they are warm. Run your palms over your hair without actually touching it. This should help control the static.</li></ul>
        <h4>Swimming</h4>
        <p>It is not recommended that you swim with extension hair. However if you do, the following precautions are recommended.</p>
        <ul><li>• Never wear a swimming cap or anything that covers your hair, the friction may cause matting.</li><li>• Before swimming comb out tangles.</li><li>• Braid hair into one braid at back of neck.</li><li>• Try to keep head above water.</li><li>• Do not swim under water.</li><li>• No diving.</li></ul>
      </div>
      <div class="spec-col">
        <ul><li>• After swimming keep head out of shower.</li><li>• Immediately after showering undo braid, comb hair and let air-dry.</li><li>• Follow with appropriate shampooing and conditioning as needed.</li></ul>
        <h4>Sauna</h4>
        <ul><li>• The water of the sauna will penetrate the hair and wet it.</li><li>• Do not wrap hair in towel, which will compress it.</li><li>• After sauna keep head out of shower.</li></ul>
        <h4>Sunbathing</h4>
        <ul><li>• After sunbathing do not unbraid until hair has cooled down.</li><li>• After hair cools, undo braid, comb hair.</li></ul>
      </div>
    </div>
  </div>
  <div class="page page--pinkfoot">
    <div class="photo misc-photo" role="img" aria-label="Model with long straight auburn hair"></div>
    <h2 class="heading misc-head">Miscellaneous Tips</h2>
    <ul class="misc-text">
      <li>• Although the extension hair is real, it is not receiving nutrients from the scalp like your own hair. Heat is your hair extensions' biggest enemy. The more you use on it, the shorter the life span of your hair. We cannot guarantee that the hair will remain silky if you use the blow dryer, flat iron or curling iron often.</li>
      <li>• When you sleep, we highly recommend that you braid, wrap or ponytail your hair together to prevent tangling. This will save time that would be spent untangling the hair the next morning.</li>
      <li>• When washing the hair, always wash it going in a downward motion. Use your fingers in a horizontal motion between wefts to clean your scalp. When rinsing, do the same to be sure all shampoo and conditioner residues are washed out.</li>
    </ul>
    <div class="brand misc-brand">Velvet Crown Tresses</div>
  </div>
</section>

</body>
</html>
```